Corvale Homes

To produce a business card design for our newly established house building and development company, We have had a logo design done please see attached, our slogan is "building your home sweet home"
Contact Information for Business Card
Adress on card needs to Read - 58 Elmsworth Lane, Lowmarsh, Westvale XV4 7QT. Director name Dean Vascotti
Requirements
Must have
- Web adress is www.corvale-homes.co.uk
- Email address is info@corvale-homes.co.uk
- phone number 07700 900417

```html
<!DOCTYPE html>
<html lang="en">
<head>
<meta charset="utf-8">
<title>Corvale Homes – Business Card</title>
<link rel="stylesheet" href="https://fonts.googleapis.com/css2?family=Work+Sans:wght@400;500;600&display=swap">
<style>
  :root {
    --backdrop: #1c1c1d;
    --card: #1a1a1b;
    --card-edge: #262627;
    --ink-emboss: #0d0d0e;
    --ink-foil: #e4e4e6;
    --ink-soft: #c9c9cc;
    --ink-muted: #8c8c90;
    --divider: #8a8a8e;
    --icon: #a0a0a4;
  }
  * { box-sizing: border-box; margin: 0; padding: 0; }
  html, body {
    width: 1200px; height: 900px; overflow: hidden;
    background: var(--backdrop);
    font-family: "Work Sans", Arial, sans-serif;
  }
  .canvas { position: relative; width: 1200px; height: 900px; }
  .card {
    position: absolute; left: 290px; width: 620px; height: 354px;
    background: linear-gradient(135deg, #202021 0%, var(--card) 60%, #151516 100%);
    border: 1px solid var(--card-edge);
    box-shadow: 0 18px 40px rgba(0,0,0,.55);
  }
  .card--front { top: 70px; }
  .card--back { top: 476px; }

  .brand-name {
    font-weight: 600; text-transform: uppercase; letter-spacing: 2px;
    line-height: 1; white-space: nowrap;
  }
  .card--front .brand-name {
    position: absolute; left: 0; right: 0; top: 150px;
    text-align: center; font-size: 44px; color: var(--ink-foil);
  }
  .card--back .brand-name {
    position: absolute; left: 14px; top: 160px; width: 262px;
    text-align: center; font-size: 27px; color: var(--ink-emboss);
  }

  .divider {
    position: absolute; left: 284px; top: 50px; width: 1.5px; height: 252px;
    background: var(--divider);
  }
  .contact { position: absolute; left: 312px; top: 58px; color: var(--ink-soft); }
  .contact__name {
    font-size: 27px; font-weight: 600; text-transform: uppercase;
    letter-spacing: 1px; line-height: 1.1; color: var(--ink-foil);
  }
  .contact__role { font-size: 15px; color: var(--ink-muted); margin-top: 2px; }
  .contact__address {
    font-size: 15.5px; line-height: 22px; margin-top: 22px;
    letter-spacing: .3px; white-space: nowrap;
  }
  .contact__list { list-style: none; margin-top: 6px; }
  .contact__item {
    display: flex; align-items: center; gap: 12px; white-space: nowrap;
    font-size: 17px; line-height: 25px; letter-spacing: .6px; color: var(--ink-foil);
  }
  .contact__icon { width: 12px; height: 12px; flex: none; }
</style>
</head>
<body>
<main class="canvas">
  <section class="card card--front" aria-label="Card front">
    <p class="brand-name">Corvale Homes</p>
  </section>

  <section class="card card--back" aria-label="Card back">
    <p class="brand-name">Corvale Homes</p>
    <div class="divider"></div>
    <div class="contact">
      <h1 class="contact__name">Dean Vascotti</h1>
      <p class="contact__role">Director</p>
      <p class="contact__address">58 Elmsworth Lane, Lowmarsh,<br>Westvale XV4 7QT.</p>
      <ul class="contact__list">
        <li class="contact__item">
          <svg class="contact__icon" viewBox="0 0 12 12"><rect x="3" y="0.8" width="6" height="10.4" rx="1" fill="none" stroke="#a0a0a4" stroke-width="1.2"/></svg>
          07700 900417
        </li>
        <li class="contact__item">
          <svg class="contact__icon" viewBox="0 0 12 12"><path d="M2.5 1.2l2 0 1 2.6-1.3 1c.6 1.3 1.6 2.3 2.9 2.9l1-1.3 2.6 1v2c0 .5-.4.9-.9.9C5.4 10.3 1.6 6.6 1.6 2.1c0-.5.4-.9.9-.9z" fill="#a0a0a4"/></svg>
          07700 900582
        </li>
        <li class="contact__item">
          <svg class="contact__icon" viewBox="0 0 12 12"><rect x="1" y="2.5" width="10" height="7" fill="none" stroke="#a0a0a4" stroke-width="1.1"/><path d="M1 2.5l5 4 5-4" fill="none" stroke="#a0a0a4" stroke-width="1.1"/></svg>
          info@corvale-homes.co.uk
        </li>
        <li class="contact__item">
          <svg class="contact__icon" viewBox="0 0 12 12"><circle cx="6" cy="6" r="5" fill="none" stroke="#a0a0a4" stroke-width="1.1"/><path d="M1 6h10M6 1c-2.2 2.8-2.2 7.2 0 10M6 1c2.2 2.8 2.2 7.2 0 10" fill="none" stroke="#a0a0a4" stroke-width=".9"/></svg>
          www.corvale-homes.co.uk
        </li>
      </ul>
    </div>
  </section>
</main>
</body>
</html>
```